Fahrzeugbeschriftung für Potovoltaik-Solaranlagen
Zielgruppe
PV-Solaranlagen für Privat, Gewerbe und Industrie
Aufgabenstellung
existierendes Logo und einen 'flotten Spruch', etwa:'....Solaranlagen vom Profi“ Brandauer Strom-Technik GmbH, Meisterbetrieb Beschriftung soll nur am Heck von Falko Reisebus R4.2 angebracht werden
Das Fzg. Hat rundum Scheiben und ist Schwarz.

```html
<!DOCTYPE html>
<html lang="de">
<head>
<meta charset="utf-8">
<title>Heckbeschriftung – Brandauer Strom-Technik</title>
<link href="https://fonts.googleapis.com/css2?family=Exo+2:wght@400;600;700&display=swap" rel="stylesheet">
<style>
  :root {
    --backdrop: #b7b7b7;
    --navy: #243247;
    --green: #a4c82a;
    --green-deep: #67b43b;
    --yellow: #f7dc22;
    --white: #ffffff;
  }
  * { margin: 0; padding: 0; box-sizing: border-box; }
  html, body {
    width: 1200px; height: 1117px; overflow: hidden;
    background: var(--backdrop);
  }
  .banner {
    position: absolute; left: 72px; top: 359px;
    width: 1056px; height: 399px;
    background: var(--navy);
    overflow: hidden;
    font-family: "Exo 2", sans-serif;
  }
  .corner-wedge { position: absolute; left: 0; top: 0; }
  .brand {
    position: absolute; left: 107px; top: 192px;
    color: var(--white);
  }
  .brand-name {
    display: flex; align-items: center; gap: 14px;
    font-size: 60px; font-weight: 600; line-height: 1; letter-spacing: 1px;
  }
  .brand-dot {
    width: 38px; height: 38px; border-radius: 50%;
    background: var(--green);
  }
  .brand-tagline {
    font-size: 28px; font-weight: 400; margin-top: 8px; margin-left: 52px;
  }
  .headline {
    position: absolute; left: 580px; top: 104px;
    color: var(--white);
    font-size: 52px; font-weight: 700; line-height: 48px; letter-spacing: 1px;
  }
  .claim {
    position: absolute; left: 580px; top: 208px;
    color: var(--green);
    font-size: 38px; font-weight: 400; line-height: 38px;
  }
  .web-pill {
    position: absolute; left: 735px; top: 323px;
    width: 321px; height: 41px;
    border-radius: 21px 0 0 21px;
    background: linear-gradient(90deg, var(--green), var(--green-deep));
    color: var(--navy);
    font-size: 21px; font-weight: 700;
    display: flex; align-items: center; justify-content: center;
  }
</style>
</head>
<body>
  <main class="banner">
    <svg class="corner-wedge" width="100" height="120" viewBox="0 0 100 120" aria-hidden="true">
      <defs>
        <linearGradient id="wedgeFill" x1="0" y1="1" x2="1" y2="0">
          <stop offset="0" stop-color="#3fa57a"/>
          <stop offset="1" stop-color="#67b43b"/>
        </linearGradient>
      </defs>
      <path d="M0 0 H96 Q40 45 0 115 Z" fill="url(#wedgeFill)"/>
    </svg>

    <div class="brand">
      <div class="brand-name"><span class="brand-dot"></span>BRANDAUER</div>
      <div class="brand-tagline">Strom-Technik</div>
    </div>

    <h1 class="headline">FOTOVOLTAIK<br>SOLARANLAGEN</h1>
    <p class="claim">KAUFT MAN AM BESTEN<br>BEIM FACHMANN</p>

    <div class="web-pill">www.brandauer-strom.de</div>
  </main>
</body>
</html>
```